Milo Castell Moving DL Flyer

We need a double sided DL flyer to give to patients to let them know that we are moving location.
On one side we would like it to read:
"We Are Moving!" and "November 2017" and our logo.
On the other side we would like it to read:
"Same Great Staff"
"Same Great Service"
"Bigger, Brighter and Better"
"New Location at 42 Quarry Rd"
with a map below (attached)
The flyer should follow our practice branding. Attached is a copy of our business card as an example of this.

```html
<!DOCTYPE html>
<html lang="en">
<head>
<meta charset="utf-8">
<title>Milo Castell Optometry – Moving Flyer</title>
<link rel="stylesheet" href="https://fonts.googleapis.com/css2?family=Montserrat:ital,wght@0,500;0,600;0,700;1,900&family=Kalam:wght@700&family=Libre+Baskerville:wght@700&display=swap">
<style>
  :root {
    --page: #e8e7ea;
    --plum: #4a3757;
    --plum-deep: #3f2e4b;
    --plum-light: #6f5886;
    --white: #ffffff;
    --ink: #2a2a2a;
    --map-grey: #c9c6cc;
  }
  * { box-sizing: border-box; margin: 0; padding: 0; }
  html, body {
    width: 1098px; height: 1200px; overflow: hidden;
    background: var(--page);
    font-family: "Montserrat", Arial, sans-serif;
  }
  .flyer {
    position: absolute; left: 104px; width: 890px; height: 420px;
    background: var(--plum); overflow: hidden;
    box-shadow: 0 6px 18px rgba(0,0,0,.25);
  }
  .flyer--front { top: 160px; }
  .flyer--back  { top: 622px; height: 418px; }
  .flyer__bg { position: absolute; inset: 0; width: 100%; height: 100%; }

  .brand-name {
    position: absolute; color: var(--ink); font-weight: 500; line-height: 1.05;
  }
  .flyer--front .brand-name { left: 28px; top: 40px; font-size: 30px; }
  .flyer--back .brand-name { left: 214px; top: 250px; font-size: 26px; color: var(--white); }

  .headline {
    position: absolute; left: 250px; width: 620px; text-align: center;
    color: var(--white); font-weight: 900; font-style: italic; line-height: .95;
    text-shadow: 6px 6px 8px rgba(20,10,30,.55);
  }
  .headline__top { top: 118px; font-size: 96px; }
  .headline__main { top: 205px; font-size: 122px; }

  .date-pill {
    position: absolute; left: 394px; top: 344px; width: 313px; height: 49px;
    background: var(--white); border-radius: 25px;
    display: flex; align-items: center; justify-content: center;
    font-family: "Libre Baskerville", Georgia, serif; font-weight: 700;
    font-size: 25px; color: var(--plum-deep);
  }

  .promise { position: absolute; left: 46px; color: var(--white); font-family: "Kalam", cursive; line-height: 1; }
  .promise__small { font-size: 15px; display: block; margin-left: 44px; }
  .promise__big { font-size: 40px; display: block; }
  .promise--staff { top: 70px; }
  .promise--service { top: 176px; }
  .divider { position: absolute; left: 46px; top: 158px; width: 264px; height: 3px; background: linear-gradient(90deg, var(--white) 60%, rgba(255,255,255,0)); }

  .benefits { position: absolute; left: 46px; top: 236px; list-style: none; color: var(--white); font-weight: 600; font-size: 25px; line-height: 29px; }
  .benefits li { display: flex; align-items: center; gap: 8px; }
  .benefits svg { width: 20px; height: 20px; }

  .location-pill {
    position: absolute; left: 0; top: 338px; width: 397px; height: 44px;
    background: var(--white); border-radius: 0 22px 22px 0;
    display: flex; align-items: center; padding-left: 46px;
    font-weight: 700; font-size: 20px; color: var(--plum-deep);
  }

  .map {
    position: absolute; left: 505px; top: 23px; width: 369px; height: 378px;
    background: linear-gradient(135deg, var(--map-grey), #e39a9e 70%, #d98a90);
  }
</style>
</head>
<body>
  <section class="flyer flyer--front">
    <svg class="flyer__bg" viewBox="0 0 890 420" preserveAspectRatio="none" aria-hidden="true">
      <path d="M0 0 H890 V34 C700 20 520 60 380 120 C250 175 120 200 0 222 Z" fill="var(--white)"/>
      <path d="M0 222 C120 200 250 175 380 120 C520 60 700 20 890 34 V50 C700 36 520 76 385 134 C255 190 125 214 0 236 Z" fill="var(--plum-light)"/>
    </svg>
    <p class="brand-name">Milo Castell<br>Optometry</p>
    <h1 class="headline headline__top">WE ARE</h1>
    <h1 class="headline headline__main">MOVING!</h1>
    <div class="date-pill">NOVEMBER 2017</div>
  </section>

  <section class="flyer flyer--back">
    <svg class="flyer__bg" viewBox="0 0 890 418" preserveAspectRatio="none" aria-hidden="true">
      <path d="M0 0 H890 V418 H0 Z" fill="var(--plum)"/>
      <path d="M0 0 H890 V110 C760 70 600 40 480 46 C300 34 150 40 0 62 Z" fill="var(--white)"/>
      <path d="M0 62 C150 40 300 34 480 46 C600 40 760 70 890 110 V122 C760 84 600 56 480 60 C300 48 150 54 0 76 Z" fill="var(--plum-light)"/>
      <path d="M890 212 C840 214 760 230 700 260 V418 H890 Z" fill="var(--plum-light)" opacity=".55"/>
    </svg>
    <p class="promise promise--staff"><span class="promise__small">Same</span><span class="promise__big">Great Staff</span></p>
    <div class="divider"></div>
    <p class="promise promise--service"><span class="promise__small">Same</span><span class="promise__big">Great Service</span></p>
    <ul class="benefits">
      <li><svg viewBox="0 0 20 20"><path d="M3 11 L8 16 L17 4" fill="none" stroke="var(--white)" stroke-width="3"/></svg>Bigger</li>
      <li><svg viewBox="0 0 20 20"><path d="M3 11 L8 16 L17 4" fill="none" stroke="var(--white)" stroke-width="3"/></svg>Brighter</li>
      <li><svg viewBox="0 0 20 20"><path d="M3 11 L8 16 L17 4" fill="none" stroke="var(--white)" stroke-width="3"/></svg>&amp; Better</li>
    </ul>
    <p class="brand-name">Milo Castell<br>Optometry</p>
    <div class="location-pill">New Location at 42 Quarry Rd</div>
    <div class="map" role="img" aria-label="Street map showing the new practice location beside the marketplace and car parking"></div>
  </section>
</body>
</html>
```